Website for an electrical contractor :)

We are after a web site which can show pictures of our jobs and our capability in a professional, creative and easily understood way.

----- Brightmoor Electrical ------

We really want a visually good looking website with three sections

Section one:
'Completed projects'
We have a few pictures of jobs which we've completed and would like to show off with a brief description. (see uploads)

Section two:
'Our capabilities'
Just a list of what services we offer

Section three:
We would like a 'contact us' section which people can send us a short msg and upload a file for plans to be able to send to us. We would need their name, phone number and email details. We would also need a short privacy policy saying 'we do not disclose information to third parties'.
We also want to display our contact number and postal address

Good luck :)

Target Market(s)

Adults 25 years+
Business owners
Builders
Real estate agents

Industry/Entity Type

Electrical

Colors

Designer to choose colors to be used in the design.

Requirements
Must have
• Visually appealing
Easy to understand
In the 'Completed projects' section, must have a list for each project we do i can upload pictures for it.

```html
<!DOCTYPE html>
<html lang="en">
<head>
<meta charset="utf-8">
<title>Brightmoor Electrical</title>
<link href="https://fonts.googleapis.com/css2?family=Arimo:wght@400;700&display=swap" rel="stylesheet">
<style>
  :root {
    --header-bg: #f7f7f7;
    --brand-ink: #4a4a4a;
    --nav-ink: #5a5a5a;
    --panel-bg: rgba(48, 44, 40, 0.78);
    --panel-ink: #ffffff;
    --rule: rgba(255, 255, 255, 0.85);
    --wood-light: #d9b48c;
    --wood-mid: #b98a62;
    --wood-dark: #7a5a44;
  }
  * { margin: 0; padding: 0; box-sizing: border-box; }
  html, body { width: 1200px; height: 636px; overflow: hidden; }
  body { font-family: "Arimo", Arial, sans-serif; position: relative; background: var(--header-bg); }

  .site-header {
    position: absolute; left: 0; top: 0; width: 1200px; height: 108px;
    background: var(--header-bg);
  }
  .brand {
    position: absolute; left: 65px; top: 38px;
    color: var(--brand-ink); font-size: 26px; font-weight: 400; line-height: 30px;
  }

  .main-nav {
    position: absolute; top: 34px; right: 80px;
    display: flex; gap: 27px;
  }
  .main-nav a { color: var(--nav-ink); text-decoration: none; font-size: 13.6px; }

  .hero-photo {
    position: absolute; left: 0; top: 108px; width: 1200px; height: 528px;
    background:
      radial-gradient(ellipse at 12% 35%, rgba(160, 70, 40, 0.55), transparent 40%),
      radial-gradient(ellipse at 70% 20%, rgba(110, 85, 70, 0.5), transparent 45%),
      linear-gradient(160deg, var(--wood-mid) 0%, var(--wood-light) 55%, var(--wood-mid) 80%, var(--wood-dark) 100%);
  }

  .intro-panel {
    position: absolute; left: 51px; top: 141px; width: 1096px; height: 374px;
    background: var(--panel-bg); color: var(--panel-ink);
    padding: 0 18px;
  }
  .intro-title {
    text-align: center; font-size: 32px; font-weight: 700;
    margin-top: 39px; line-height: 36px;
  }
  .intro-rule { border: 0; border-top: 1px solid var(--rule); margin-top: 18px; }
  .intro-copy { margin-top: 58px; font-size: 12.9px; line-height: 18.8px; }
  .intro-copy p + p { margin-top: 9px; }
</style>
</head>
<body>
  <header class="site-header">
    <div class="brand">Brightmoor Electrical</div>
    <nav class="main-nav">
      <a href="#projects">Completed Projects</a>
      <a href="#capabilities">Our Capabilities</a>
      <a href="#contact">Contact Us</a>
    </nav>
  </header>

  <div class="hero-photo" role="img" aria-label="Photo of a wooden desk with rulers, a notebook and a red chair"></div>

  <section class="intro-panel">
    <h1 class="intro-title">Brightmoor Electric</h1>
    <hr class="intro-rule">
    <div class="intro-copy">
      <p>Lorem ipsum dolor sit amet, neque lobortis tortor, quis est mauris amet venenatis, semper morbi aut mauris, a omnis. Consequat risus mi eu eleifend aliquam nunc, per arcu ut omnis, nascetur massa at velit, ultricies sodales placerat sem sed libero, nulla mauris ac mauris iusto lectus nisl. Pellentesque turpis lectus, in lacinia nibh fusce, urna lectus at sodales a nulla mi, urna viverra nascetur aliquet etiam nullam id. Euismod donec magnis porta praesent amet bibendum, vestibulum pede risus lacinia ac, lectus lobortis vehicula duis suspendisse, amet ullamcorper lorem vitae lacus sed sapien. Amet amet sit, diam nullam faucibus erat id, sed dapibus sollicitudin eleifend vivamus mauris arcu, sit leo proin ultricies. Ipsum id suscipit erat aliquet amet, nonummy tellus amet viverra velit, wisi elementum dignissim dui vitae augue adipiscing, pulvinar facilisi at tellus ut, rutrum eu. Aenean tellus nunc quis purus vehicula sit. Faucibus praesent viverra lacin ia ut. Lobortis nec culpa leo, nam sed nulla vestibulum. Non sed voluptas sodales. Condimentum enim integer etiam semper gravida. Velit pulvinar sodales mattis ut tellus.</p>
      <p>Pede elementum magna, praesent sem ante mi placerat, et torquent, in class fringilla purus blandit hac, ut pellentesque morbi mi. Quasi voluptates vitae morbi feugiat, amet tempor tincidunt do vestibulum, ultricies ut diam faucibus arcu erat. Ac amet proin vel ut, convallis pede, sit urna mus, deserunt eget amet risus tortor vehicula. Duis facilisi. Fusce et, neque magna, eget netus, a vestibulum id, omnis dui nulla id est. Sed neque, ornare potenti ridiculus, sed eu mattis non malesuada dolor erat.</p>
    </div>
  </section>
</body>
</html>
```